KVO-Business Card Design

I need a modern, professional business card design that includes my logo as the main feature, maybe the entire background with the contact info overlaying or even contact info on the back and the logo full frontal

Neat and organized placement of contact information

Would like to see options in black and white

Target Market(s)

real estate Developers, Construction managers, business and home owners

Industry/Entity Type

Construction

Contact Information for Business Card

KVO Construction
Danny Ferrante
General Contractor

Office: 1-888-902-7315 Ext #1
Cell: 215-730-4162
Fax: 1-888-902-7315

Font styles to use
Serif

Requirements
Must have
• title
• office #
• cell #
• Email
• website
Nice to have
• fax

```html
<!DOCTYPE html>
<html lang="en">
<head>
<meta charset="utf-8">
<title>KVO Construction – Business Cards</title>
<link rel="stylesheet" href="https://fonts.googleapis.com/css2?family=Roboto:wght@400;500;700&display=swap">
<style>
  :root {
    --stage: #e9e7e2;
    --paper: #ffffff;
    --ink: #1f1f1f;
    --night: #050505;
    --green-deep: #137a3c;
    --green: #1e8f45;
    --green-light: #6cc04a;
    --muted: #9a9a9a;
  }
  * { margin: 0; padding: 0; box-sizing: border-box; }
  html, body { width: 1200px; height: 1023px; overflow: hidden; }
  body {
    background: var(--stage);
    font-family: "Roboto", Arial, sans-serif;
    position: relative;
  }
  .card {
    position: absolute;
    left: 180px;
    width: 840px;
    height: 480px;
    border-radius: 4px;
    overflow: hidden;
    box-shadow: 0 6px 18px rgba(0,0,0,.18);
  }
  .card--front { top: 22px; background: var(--paper); }
  .card--back { top: 522px; background: var(--night); }

  .band { position: absolute; left: 0; bottom: 0; width: 840px; height: 130px; }

  .brand {
    position: absolute;
    display: flex;
    align-items: center;
    gap: 16px;
    font-weight: 700;
    letter-spacing: 2px;
    text-transform: uppercase;
    color: var(--green);
    white-space: nowrap;
  }
  .brand__mark { width: 34px; height: 34px; background: var(--green); border-radius: 50%; flex: none; }
  .brand__name { font-size: 40px; line-height: 1; }

  .card--front .brand { left: 48px; top: 218px; gap: 12px; }
  .card--front .brand__mark { width: 28px; height: 28px; }
  .card--front .brand__name { font-size: 30px; letter-spacing: 1.5px; }
  .card--back .brand { left: 0; right: 0; top: 170px; justify-content: center; color: var(--green-light); }
  .card--back .brand__mark { background: var(--green-light); }

  .person { position: absolute; right: 56px; top: 44px; display: flex; gap: 14px; align-items: flex-start; }
  .person__text { text-align: right; }
  .person__name { font-size: 34px; font-weight: 400; color: var(--ink); line-height: 1.1; }
  .person__title { font-size: 20px; font-weight: 700; color: var(--green); margin-top: 2px; }
  .person__icon { width: 38px; height: 38px; }

  .divider { position: absolute; left: 460px; top: 170px; width: 1px; height: 140px; background: var(--green); }

  .contacts { position: absolute; left: 488px; top: 150px; list-style: none; }
  .contacts li { display: flex; align-items: center; gap: 12px; font-size: 21px; color: var(--ink); height: 36px; }
  .contacts svg { width: 24px; height: 24px; flex: none; }

  .website {
    position: absolute;
    left: 60px;
    bottom: 38px;
    font-size: 24px;
    letter-spacing: .5px;
    color: #ffffff;
  }
  .card--back .website { bottom: 24px; font-size: 22px; }
</style>
</head>
<body>

<section class="card card--front" aria-label="Card front">
  <svg class="band" viewBox="0 0 840 130" aria-hidden="true">
    <path d="M0 40 H440 C490 40 500 100 550 100 H840 V130 H0 Z" fill="var(--green-deep)"/>
  </svg>

  <div class="brand">
    <span class="brand__mark"></span>
    <span class="brand__name">KVO Construction</span>
  </div>

  <div class="person">
    <div class="person__text">
      <p class="person__name">Danny Ferrante</p>
      <p class="person__title">General Contractor</p>
    </div>
    <svg class="person__icon" viewBox="0 0 38 38" aria-hidden="true">
      <rect width="38" height="38" rx="7" fill="var(--green)"/>
      <circle cx="19" cy="13" r="5.5" fill="#fff"/>
      <path d="M9 31 C9 23 14 20 19 20 C24 20 29 23 29 31 Z" fill="#fff"/>
    </svg>
  </div>

  <span class="divider"></span>

  <ul class="contacts">
    <li>
      <svg viewBox="0 0 24 24" aria-hidden="true"><rect width="24" height="24" rx="5" fill="var(--green-light)"/><path d="M8 6 L10 6 L11 9 L9.5 10.5 C10.5 12.5 11.5 13.5 13.5 14.5 L15 13 L18 14 L18 16 C18 17 17 18 16 18 C10.5 17.5 6.5 13.5 6 8 C6 7 7 6 8 6 Z" fill="#fff"/></svg>
      215-730-4162
    </li>
    <li>
      <svg viewBox="0 0 24 24" aria-hidden="true"><rect width="24" height="24" rx="5" fill="var(--green-light)"/><rect x="8" y="5" width="8" height="14" rx="1.5" fill="#fff"/><rect x="10" y="7" width="4" height="8" fill="var(--green-light)"/></svg>
      1-888-902-7315 Ext #1
    </li>
    <li>
      <svg viewBox="0 0 24 24" aria-hidden="true"><rect width="24" height="24" rx="5" fill="var(--green-light)"/><rect x="8" y="5" width="8" height="5" fill="#fff"/><rect x="5" y="10" width="14" height="7" rx="1" fill="#fff"/><rect x="8" y="15" width="8" height="4" fill="#fff" stroke="var(--green-light)"/></svg>
      1-888-902-7315
    </li>
    <li>
      <svg viewBox="0 0 24 24" aria-hidden="true"><rect width="24" height="24" rx="5" fill="var(--green-light)"/><rect x="5" y="7" width="14" height="10" fill="#fff"/><path d="M5 7 L12 13 L19 7" fill="none" stroke="var(--green-light)" stroke-width="1.5"/></svg>
      hello@kvoconstruction.com
    </li>
  </ul>

  <p class="website">www.website.com</p>
</section>

<section class="card card--back" aria-label="Card back">
  <svg class="band" viewBox="0 0 840 130" aria-hidden="true">
    <path d="M0 60 H400 C450 60 460 112 510 112 H840 V130 H0 Z" fill="var(--green-deep)"/>
  </svg>

  <div class="brand">
    <span class="brand__mark"></span>
    <span class="brand__name">KVO Construction</span>
  </div>

  <p class="website">www.yourwebsite.com</p>
</section>

</body>
</html>
```